Business card design needed

After a business card which portrays the same precision tig welding and performance fabrications we offer customers. Catering mainly for the automotive market, but process work for marine, industrial & hospitality work is definitely welcome.

We provide the same level quality, care and workmanship regardless of how big or small the job is. Quality is the first and foremost for customers looking for the highest standards around along with a customised look not found anywhere else.

Our offering is tailor made for each customer and where needed, a completely individual look

Colours - red, black and white (as per the attached logo)

The design should portray a customised/one-off solution for each customer with a high attention to detail.
Updates

The brief should have included this design is required for a 2 sided card

Industry/Entity Type

Hospitality

Contact Information for Business Card

Blue Anchor Metalworks
3/14 Corwen Hale Avenue
North Wollongong NSW 2500

Ph: 02 4871 3064
Mob: 0412 586 137
Email: blueanchormetalworks@mailhaven.example
Facebook: www.socialpage.example/blueanchormetalworks

Requirements
Must have
• Must have a catchy front side without being cluttered & brief but list off main offerings on the back. For eg
- customised concept & design for each project
- 2D & 3D modelling & machining
- catering for single or mass prodcued items

```html
<!DOCTYPE html>
<html lang="en">
<head>
<meta charset="utf-8">
<title>Blue Anchor Metalworks – Business Card</title>
<link href="https://fonts.googleapis.com/css2?family=Ubuntu:wght@400;700&display=swap" rel="stylesheet">
<style>
  :root {
    --stage: #d9d9db;
    --card: #25272a;
    --card-edge: #1b1c1e;
    --white: #ffffff;
    --text: #e9e9e9;
    --red: #d8242f;
    --photo-a: #6d6a5c;
    --photo-b: #9aa0a5;
    --photo-c: #3b4047;
  }
  * { margin: 0; padding: 0; box-sizing: border-box; }
  html, body { width: 1200px; height: 861px; overflow: hidden; }
  body {
    background: var(--stage);
    font-family: "Ubuntu", Arial, sans-serif;
    position: relative;
  }
  .card {
    position: absolute;
    top: 266px;
    width: 540px;
    height: 330px;
    background: linear-gradient(180deg, #2c2e31 0%, var(--card) 55%, var(--card-edge) 100%);
    overflow: hidden;
    box-shadow: 0 10px 30px rgba(0,0,0,0.25);
  }
  .card--back { left: 40px; }
  .card--front { left: 620px; }
  .card__chevron { position: absolute; top: 0; left: 0; width: 540px; height: 330px; }

  .photo-strip {
    position: absolute;
    top: 40px; left: 0;
    width: 452px; height: 82px;
    background: linear-gradient(90deg, var(--photo-a) 0%, var(--photo-b) 30%, var(--photo-c) 55%, var(--photo-b) 78%, var(--photo-c) 100%);
  }
  .brand-name {
    color: var(--white);
    font-weight: 700;
    letter-spacing: 0.5px;
    white-space: nowrap;
    display: flex;
    align-items: center;
  }
  .brand-name__dot {
    display: inline-block;
    width: 12px; height: 12px;
    border-radius: 50%;
    background: var(--red);
    margin-right: 10px;
  }
  .card--back .brand-name {
    position: absolute;
    top: 150px; left: 0; width: 452px;
    justify-content: center;
    font-size: 22px;
  }
  .about {
    position: absolute;
    top: 200px; left: 20px; width: 412px;
    color: var(--text);
    font-size: 12.5px;
    line-height: 1.3;
    text-align: center;
  }
  .about p + p { margin-top: 12px; }

  .card--front .brand-name {
    position: absolute;
    top: 66px; left: 150px; width: 380px;
    justify-content: center;
    font-size: 25px;
  }
  .contact-list {
    position: absolute;
    top: 168px; left: 170px;
    list-style: none;
    color: var(--text);
    font-size: 12.5px;
  }
  .contact-list li {
    display: flex; align-items: center;
    height: 23px;
    white-space: nowrap;
  }
  .contact-list svg { width: 15px; height: 15px; margin-right: 10px; flex: none; }
</style>
</head>
<body>

<section class="card card--back" aria-label="Business card back">
  <svg class="card__chevron" viewBox="0 0 540 330" aria-hidden="true">
    <polygon points="452,0 540,0 540,330 452,330 502,165" fill="#f0f0f0"/>
    <polygon points="458,0 540,0 540,330 458,330 508,165" fill="#7e7f82"/>
    <polygon points="476,0 540,0 540,330 476,330 526,165" fill="#b9babc"/>
    <polygon points="496,0 540,0 540,330 496,330 546,165" fill="#646568"/>
    <polygon points="516,0 540,0 540,330 516,330 566,165" fill="#d0d1d3"/>
  </svg>
  <div class="photo-strip" role="img" aria-label="Row of workshop photos: welded aluminium tanks, intercooler, turbo pipework and TIG welding"></div>
  <div class="brand-name"><span class="brand-name__dot"></span>Blue Anchor Metalworks</div>
  <div class="about">
    <p>We provide the same level quality, care and workmanship regardless of how big or small the job is. Quality is the first and foremost for customers looking for the highest standards around along with a customised look not found anywhere else.</p>
    <p>We offer tailor made for each customer and where needed, a completely individual look.</p>
  </div>
</section>

<section class="card card--front" aria-label="Business card front">
  <svg class="card__chevron" viewBox="0 0 540 330" aria-hidden="true">
    <polygon points="0,0 96,0 146,165 96,330 0,330" fill="#f0f0f0"/>
    <polygon points="0,0 90,0 140,165 90,330 0,330" fill="#707174"/>
    <polygon points="0,0 68,0 118,165 68,330 0,330" fill="#bdbec0"/>
    <polygon points="0,0 44,0 94,165 44,330 0,330" fill="#5d5e61"/>
    <polygon points="0,0 20,0 70,165 20,330 0,330" fill="#d2d3d5"/>
  </svg>
  <div class="brand-name"><span class="brand-name__dot"></span>Blue Anchor Metalworks</div>
  <ul class="contact-list">
    <li>
      <svg viewBox="0 0 16 16" aria-hidden="true"><circle cx="8" cy="8" r="8" fill="var(--red)"/><path d="M8 3.5a2.8 2.8 0 0 0-2.8 2.8c0 2.2 2.8 5.7 2.8 5.7s2.8-3.5 2.8-5.7A2.8 2.8 0 0 0 8 3.5zm0 3.9a1.1 1.1 0 1 1 0-2.2 1.1 1.1 0 0 1 0 2.2z" fill="#fff"/></svg>
      3/14 Corwen Hale Avenue North Wollongong NSW 2500
    </li>
    <li>
      <svg viewBox="0 0 16 16" aria-hidden="true"><circle cx="8" cy="8" r="8" fill="var(--red)"/><path d="M5.2 4h1.6l.8 2-1 .8a5.5 5.5 0 0 0 2.6 2.6l.8-1 2 .8v1.6c0 .5-.4.8-.9.8A7.4 7.4 0 0 1 4.4 4.9c0-.5.3-.9.8-.9z" fill="#fff"/></svg>
      02 4871 3064
    </li>
    <li>
      <svg viewBox="0 0 16 16" aria-hidden="true"><circle cx="8" cy="8" r="8" fill="var(--red)"/><rect x="5.5" y="3.5" width="5" height="9" rx="1" fill="#fff"/><rect x="6.4" y="4.6" width="3.2" height="5.6" fill="var(--red)"/></svg>
      0412 586 137
    </li>
    <li>
      <svg viewBox="0 0 16 16" aria-hidden="true"><circle cx="8" cy="8" r="8" fill="var(--red)"/><rect x="4" y="5" width="8" height="6" rx="0.6" fill="#fff"/><path d="M4.3 5.3 8 8.3l3.7-3" fill="none" stroke="var(--red)" stroke-width="0.9"/></svg>
      blueanchormetalworks@mailhaven.example
    </li>
    <li>
      <svg viewBox="0 0 16 16" aria-hidden="true"><circle cx="8" cy="8" r="8" fill="var(--red)"/></svg>
      www.socialpage.example/blueanchormetalworks
    </li>
  </ul>
</section>

</body>
</html>
```